Have photos and logo just need help with web banner

Dimensions: 950 width by 425 height, pixels
Resolution: 92 DPI
Layout: Landscape
Format: JPG

Target Market(s)

Luxury market for women 28-55

Industry/Entity Type

Landscape

Number of Pages Required

1 page

Font styles to use
Script

Requirements
Must have
• Elegant, sophisticated feel
• Tagline: bags with a silver lining
Nice to have
• Shoes bag / has athletic, strong feel
Should not have
• Not cluttered. Not confusing.

```html
<!DOCTYPE html>
<html lang="en">
<head>
<meta charset="utf-8">
<title>Bags with a Silver Lining – Banner</title>
<link href="https://fonts.googleapis.com/css2?family=Roboto+Condensed:wght@700&display=swap" rel="stylesheet">
<style>
  :root {
    --panel-dark: #262626;
    --panel-mid: #333333;
    --accent-green: #98c23c;
    --stripe-green: #5e8a2e;
    --band-light: #d3d5d8;
    --corner-black: #0c0c0c;
    --text-white: #ffffff;
    --wood: #b89a78;
    --bag-grey: #8f9193;
  }
  * { margin: 0; padding: 0; box-sizing: border-box; }
  html, body { width: 1200px; height: 537px; overflow: hidden; background: var(--panel-dark); }
  .banner {
    position: relative;
    width: 1200px;
    height: 537px;
    overflow: hidden;
    background: linear-gradient(100deg, var(--panel-mid) 0%, var(--panel-dark) 60%, #1e1e1e 100%);
    font-family: "Roboto Condensed", "Arial Narrow", sans-serif;
  }
  .product-photo {
    position: absolute;
    left: 0; top: 0;
    width: 800px; height: 537px;
    background:
      radial-gradient(ellipse 260px 230px at 320px 330px, #6d6e70 0%, #4d4e50 55%, transparent 100%),
      radial-gradient(ellipse 340px 300px at 300px 300px, var(--bag-grey) 0%, transparent 80%),
      linear-gradient(180deg, var(--wood) 0%, #a5865f 100%);
    -webkit-mask-image: linear-gradient(90deg, #000 0%, #000 68%, transparent 92%);
            mask-image: linear-gradient(90deg, #000 0%, #000 68%, transparent 92%);
  }
  .decor {
    position: absolute;
    inset: 0;
    width: 1200px; height: 537px;
  }
  .headline {
    position: absolute;
    left: 686px;
    top: 170px;
    text-transform: uppercase;
    line-height: 1;
  }
  .headline__accent {
    display: block;
    color: var(--accent-green);
    font-size: 52px;
    line-height: 56px;
    letter-spacing: 0.2px;
  }
  .tagline {
    display: block;
    margin-top: 10px;
    color: var(--text-white);
    font-size: 39px;
    line-height: 42px;
  }
  .cta {
    position: absolute;
    left: 686px;
    top: 375px;
    color: var(--accent-green);
    font-size: 20px;
    text-transform: uppercase;
    text-decoration: none;
  }
</style>
</head>
<body>
  <div class="banner">
    <div class="product-photo" role="img" aria-label="Open gray sports bag with silver lining holding a laptop and athletic shoes, on a wooden floor"></div>

    <svg class="decor" viewBox="0 0 1200 537" aria-hidden="true">
      <defs>
        <linearGradient id="topBandFade" x1="0" y1="0" x2="0" y2="1">
          <stop offset="0" stop-color="#e4e5e7" stop-opacity="0.9"/>
          <stop offset="1" stop-color="#e4e5e7" stop-opacity="0"/>
        </linearGradient>
      </defs>
      <polygon class="top-band" points="735,0 860,0 690,150 640,150" fill="url(#topBandFade)"/>
      <polygon class="light-band" points="830,537 1200,268 1200,385 990,537" fill="var(--band-light)"/>
      <polygon class="green-stripe" points="945,537 1120,412 1120,440 985,537" fill="var(--stripe-green)"/>
      <polygon class="dark-corner" points="990,537 1200,385 1200,537" fill="var(--corner-black)"/>
    </svg>

    <h1 class="headline">
      <span class="headline__accent">Elegant,</span>
      <span class="headline__accent">Sophisticated Feel</span>
      <span class="tagline">Bags with a Silver Lining</span>
    </h1>
    <a class="cta" href="#">Learn More</a>
  </div>
</body>
</html>
```